Card and board game developer website, small e-commerce site

We are designing a website for Copper Lantern Otter Works. I need a homepage and a typical inside page designed.
The website navigation will be:
Home (where we'll introduce the games and the website)
Our Games (drops open into the two games)
Griffins of Morvale Keep
Tidecraft
Order Now
About Us
Contact
The header of the website will include the logo, the navigation and a link to a facebook page. The header will also include a cart icon and a link to My Account.
Then on the homepage I suggest we include a row for each game:
Griffins of Morvale Keep
This row will include a photo (or maybe a series of photos that animate into each other) and quick info about the game plus two buttons: Info and Photos (which will go to the detail page with the photo gallery), and Order Now (which will take you to the product for ordering).
Tidecraft
Your footer will contain a copyright note, plus links to:
Terms and conditions
Shipping and returns
FAQ
Contact
Account login
NOTE: the logo is the orange mokey. I've uploaded a brief with more information. The current website that we are redesigning is here https://www.copperlanternotter.example/
Please send me any questions that you have.
Target Market(s)
People interested in fun card and board games at home.
Number of Pages Required
Look and feel

```html
<!DOCTYPE html>
<html lang="en">
<head>
<meta charset="utf-8">
<title>Copper Lantern Otter Works — Home</title>
<link href="https://fonts.googleapis.com/css2?family=Rubik:wght@500;700;800&family=Roboto:wght@400;500&display=swap" rel="stylesheet">
<style>
:root{
  --orange:#e8632b;
  --orange-deep:#d9541f;
  --sky:#c9e8ee;
  --hello-blue:#a6d4de;
  --ink:#000;
  --paper:#fff;
  --field:#f3f3f3;
  --grey-disc:#efefef;
  --text:#1a1a1a;
}
*{box-sizing:border-box;margin:0;padding:0}
html,body{width:1200px;height:2602px;overflow:hidden;background:var(--ink)}
body{font-family:"Roboto",Arial,sans-serif;color:var(--text)}
.page{position:absolute;left:205px;top:0;width:791px;height:2602px;background:var(--paper);overflow:hidden}
.abs{position:absolute}

/* header */
.site-header{position:absolute;left:0;top:0;width:791px;height:60px;z-index:3}
.brand{left:66px;top:17px;font-family:"Rubik",sans-serif;font-weight:500;font-size:21px;color:var(--orange);letter-spacing:1px}
.nav{left:255px;top:24px;display:flex;gap:20px;font-size:9px;font-weight:500;color:#111}
.nav a{color:inherit;text-decoration:none}
.nav .current{color:var(--orange)}
.header-icon{width:24px;height:24px;border-radius:50%;background:#7dc3d6;top:17px}
.header-icon svg{display:block;margin:5px auto 0}

/* hero */
.hero{left:0;top:0;width:791px;height:460px}
.hero-mark{left:246px;top:105px;width:300px;height:260px;text-align:center}
.hero-mark .disc{width:150px;height:150px;border-radius:50%;background:var(--orange);margin:0 auto 16px}
.hero-mark .name{font-family:"Rubik",sans-serif;font-weight:700;font-size:24px;color:var(--orange);line-height:1.15}

/* section headings */
.section-title{font-family:"Rubik",sans-serif;font-weight:800;color:var(--paper);text-align:center;width:791px;left:0;font-size:36px;letter-spacing:.5px;
  text-shadow:-2px -2px 0 var(--ink),2px -2px 0 var(--ink),-2px 2px 0 var(--ink),2px 2px 0 var(--ink),3px 4px 0 var(--ink)}

/* games */
.games{left:0;top:433px;width:791px;height:811px;background:var(--orange)}
.halftone{background:radial-gradient(ellipse at center,var(--orange-deep) 0%,rgba(217,84,31,0) 70%)}
.game-card{background:var(--paper);border-radius:16px;box-shadow:6px 7px 0 var(--ink)}
.game-photo{border-radius:6px}
.game-title{font-family:"Rubik",sans-serif;font-weight:700;font-size:20px;color:#111;letter-spacing:.3px}
.game-copy{font-size:9.5px;line-height:15px;color:#222}
.game-copy p+p{margin-top:14px}
.fact{display:flex;align-items:center;gap:6px;font-size:9.5px;margin-top:16px}
.fact i{width:10px;height:10px;border-radius:50%;background:var(--orange);display:inline-block}
.footnote{font-size:7px;margin-top:20px}
.btn{position:absolute;background:var(--ink);color:var(--paper);border-radius:10px;font-family:"Rubik",sans-serif;font-weight:500;font-size:12px;
  display:flex;align-items:center;justify-content:center;letter-spacing:.4px;height:42px;width:138px}

/* order */
.order{left:0;top:1244px;width:791px;height:446px;
  background:linear-gradient(135deg,#8fb59c 0%,#c6c889 25%,#6f9a8f 45%,#d9cf96 65%,#8aa6a0 85%,#c9b585 100%)}
.order-panel{left:64px;top:120px;width:661px;height:330px;background:var(--paper);border-radius:18px 18px 0 0}
.product{width:200px;text-align:center}
.product .disc{width:168px;height:168px;border-radius:50%;background:var(--grey-disc);margin:0 auto;position:relative}
.product .shot{position:absolute;border-radius:4px}
.product .label{font-size:15px;margin-top:14px;color:#111}
.product .price{font-family:"Rubik",sans-serif;font-weight:500;font-size:20px;color:#111}

/* about */
.about{left:0;top:1690px;width:791px;height:275px;background:var(--ink);color:var(--paper)}
.about h2{position:absolute;left:66px;top:54px;font-family:"Rubik",sans-serif;font-weight:700;font-size:38px}
.about .copy{position:absolute;left:66px;top:115px;width:410px;font-size:8.5px;line-height:15px}
.about .copy p+p{margin-top:14px}
.about-art{left:518px;top:37px;width:207px;height:201px;border-radius:8px;
  background:radial-gradient(circle at 50% 55%,#3f54b8 0%,#5a3f8a 45%,#a8744e 100%)}

/* contact */
.hello{left:0;top:1965px;width:791px;height:451px;background:var(--hello-blue)}
.field{left:135px;width:520px;height:30px;background:var(--field);border-radius:10px;font-size:8.5px;padding:10px 20px;color:#222}

/* footer */
.site-footer{left:0;top:2416px;width:791px;height:186px;background:var(--paper)}
.foot-mark{left:68px;top:45px;width:78px;text-align:center}
.foot-mark .disc{width:40px;height:40px;border-radius:50%;background:var(--orange);margin:0 auto 4px}
.foot-mark span{font-family:"Rubik",sans-serif;font-weight:700;font-size:8px;color:var(--orange);line-height:1.1;display:block}
.foot-col{font-size:9px;line-height:18px;color:#111}
.foot-col strong{font-weight:500}
.foot-col a{display:block;color:inherit;text-decoration:none;font-weight:500}
.social{width:33px;height:33px;border-radius:50%;background:var(--orange);top:51px}
.foot-bar{left:182px;top:147px;width:428px;height:13px;background:var(--ink);border-radius:7px}
.copyright{left:0;top:164px;width:791px;text-align:center;font-size:5.5px;color:#222}
</style>
</head>
<body>
<div class="page">

  <!-- hero -->
  <section class="abs hero">
    <svg class="abs" width="791" height="460" viewBox="0 0 791 460" aria-hidden="true" style="left:0;top:0">
      <polygon fill="var(--sky)" points="0,90 195,32 205,250 160,285 115,330 140,360 110,460 0,460"/>
      <polygon fill="var(--sky)" points="791,38 690,62 580,180 635,215 610,300 720,330 705,410 791,460"/>
    </svg>
    <div class="abs hero-mark">
      <div class="disc"></div>
      <div class="name">Copper Lantern<br>Otter Works</div>
    </div>
  </section>

  <header class="site-header">
    <div class="abs brand">CLOW</div>
    <nav class="abs nav">
      <a class="current" href="#">HOME</a>
      <a href="#">OUR GAMES</a>
      <a href="#">ORDER NOW</a>
      <a href="#">ABOUT US</a>
      <a href="#">CONTACT</a>
    </nav>
    <div class="abs header-icon" style="left:667px" aria-label="Social page"></div>
    <div class="abs header-icon" style="left:699px" aria-label="Cart">
      <svg width="14" height="13" viewBox="0 0 14 13"><path d="M1 2h2l2 6h6l2-4H4" fill="none" stroke="#fff" stroke-width="1.6"/><circle cx="6" cy="11" r="1.2" fill="#fff"/><circle cx="10" cy="11" r="1.2" fill="#fff"/></svg>
    </div>
  </header>

  <!-- our games -->
  <section class="abs games">
    <svg class="abs" width="791" height="30" viewBox="0 0 791 30" style="left:0;top:-22px" aria-hidden="true">
      <polygon fill="var(--orange)" points="0,20 120,22 160,8 230,14 280,4 300,16 420,12 470,0 520,10 620,6 700,0 791,18 791,30 0,30"/>
    </svg>
    <h2 class="abs section-title" style="top:70px">OUR GAMES</h2>

    <div class="abs halftone" style="left:0;top:150px;width:70px;height:500px"></div>
    <div class="abs halftone" style="left:520px;top:480px;width:271px;height:330px"></div>

    <article class="abs game-card" style="left:64px;top:152px;width:324px;height:578px">
      <div class="abs game-photo" role="img" aria-label="Griffins of Morvale Keep game box and board" style="left:36px;top:40px;width:272px;height:135px;background:linear-gradient(120deg,#3f6f9c,#b68a5a 55%,#6a2e3a)"></div>
      <div class="abs" style="left:22px;top:203px;width:285px">
        <h3 class="game-title">GRIFFINS OF MORVALE KEEP</h3>
        <div class="game-copy" style="margin-top:8px">
          <p>Welcome to The Griffins Of Morvale Keep, the first board game where every player is a GRIFFIN.</p>
          <p>Conquer territory and build your empire. Plunder castles and collect a huge hoard of gold. Rescue relatively attractive royalty or maybe eat them. Who knows? All we know is that everyone's a winner<br>when the pizza's delivered!**</p>
          <div class="fact"><i></i>2 - 6 players *</div>
          <div class="fact"><i></i>Playtime approximately 1.5 hours.</div>
          <p class="footnote">* Game comes with 4 griffin packs. Additional griffin expansion packs coming soon.</p>
          <p class="footnote">** Pizza sold separately. Pizza not included.</p>
        </div>
      </div>
      <a class="btn" style="left:20px;top:518px">SEE DETAIL</a>
      <a class="btn" style="left:165px;top:518px">ORDER NOW</a>
    </article>

    <article class="abs game-card" style="left:399px;top:152px;width:324px;height:499px">
      <div class="abs game-photo" role="img" aria-label="Tidecraft card deck and tuck box" style="left:45px;top:28px;width:236px;height:195px;background:linear-gradient(135deg,#5b4a2e,#8a4a3a 50%,#3b3a2a)"></div>
      <div class="abs" style="left:22px;top:256px;width:285px">
        <h3 class="game-title">TIDECRAFT</h3>
        <div class="game-copy" style="margin-top:8px">
          <p>Welcome to Tidecraft, a fast paced card game of strategy and chance. Play your element cards</p>
          <p>(Earth, Air, Fire,Water) and wild cards (Guardian, Balance, Evolution, Genesis) wisely and be the<br>first player to discard all of their cards and declare yourself the master of the elements.</p>
        </div>
      </div>
      <a class="btn" style="left:20px;top:437px">SEE DETAIL</a>
      <a class="btn" style="left:165px;top:437px">ORDER NOW</a>
    </article>
  </section>

  <!-- order now -->
  <section class="abs order" role="img" aria-label="Watercolour wash background">
    <h2 class="abs section-title" style="top:44px">ORDER NOW</h2>
    <div class="abs order-panel">
      <div class="abs product" style="left:35px;top:62px">
        <div class="disc"><div class="shot" role="img" aria-label="Tidecraft deck box" style="left:30px;top:-8px;width:110px;height:160px;background:linear-gradient(160deg,#4a3a2a,#8a3a2a)"></div></div>
        <div class="label">Tidecraft</div>
        <div class="price">$ 14.95</div>
      </div>
      <div class="abs product" style="left:233px;top:62px">
        <div class="disc"><div class="shot" role="img" aria-label="Griffins of Morvale Keep game box" style="left:0;top:35px;width:170px;height:95px;background:linear-gradient(120deg,#3f6f9c,#b68a5a 55%,#6a2e3a)"></div></div>
        <div class="label">Griffins of Morvale Keep</div>
        <div class="price">$ 54.95</div>
      </div>
      <div class="abs product" style="left:432px;top:62px">
        <div class="disc"><div class="shot" role="img" aria-label="Grey studio T-shirt" style="left:10px;top:-2px;width:150px;height:165px;background:linear-gradient(180deg,#cfcfcf,#b9b9b9)"></div></div>
        <div class="label">CLOW&nbsp; T-shirt</div>
        <div class="price">$ 19.95</div>
      </div>
    </div>
  </section>

  <!-- about -->
  <section class="abs about">
    <svg class="abs" width="791" height="275" viewBox="0 0 791 275" aria-hidden="true" style="left:0;top:0">
      <path d="M725 50 Q760 40 791 55" fill="none" stroke="#a6d4de" stroke-width="1.5"/>
      <path d="M725 195 Q765 190 791 215" fill="none" stroke="#a6d4de" stroke-width="1.5"/>
      <path d="M575 238 Q578 260 582 275" fill="none" stroke="#a6d4de" stroke-width="1.5"/>
      <path d="M640 238 Q632 258 630 275" fill="none" stroke="#a6d4de" stroke-width="1.5"/>
    </svg>
    <h2>ABOUT US</h2>
    <div class="copy">
      <p>They say do what you love...At Copper Lantern Otter Works we love to dream big dreams and bring those dreams to life. We create games to entertain and engage the people that play them; games that invite and inspire players to add a bit of themselves to each game, and how it is played.</p>
      <p>Come play with us.</p>
    </div>
    <div class="abs about-art" role="img" aria-label="Painted blue griffin rising from a lotus flower"></div>
  </section>

  <!-- say hello -->
  <section class="abs hello">
    <h2 class="abs section-title" style="top:56px">SAY HELLO</h2>
    <div class="abs field" style="top:134px">Name</div>
    <div class="abs field" style="top:180px">Email</div>
    <div class="abs field" style="top:225px">Subjet</div>
    <div class="abs field" style="top:269px;height:63px">Message</div>
    <a class="btn" style="left:326px;top:359px">SUBMIT</a>
  </section>

  <!-- footer -->
  <footer class="abs site-footer">
    <div class="abs foot-mark"><div class="disc"></div><span>Copper Lantern Otter Works</span></div>
    <div class="abs foot-col" style="left:162px;top:52px;line-height:15px;font-size:8.5px">
      <strong>Copper Lantern Otter Works</strong><br>PO BOX 812<br>Fernbrook Hollow, OR<br>97555-0812
    </div>
    <div class="abs foot-col" style="left:335px;top:50px"><a href="#">Terms and conditions</a><a href="#">Shipping and returns</a><a href="#">FAQ</a></div>
    <div class="abs foot-col" style="left:472px;top:50px"><a href="#">Contact</a><a href="#">Account Login</a></div>
    <div class="abs social" style="left:600px" aria-label="Social link"></div>
    <div class="abs social" style="left:646px" aria-label="Social link"></div>
    <div class="abs social" style="left:692px" aria-label="Social link"></div>
    <div class="abs foot-bar"></div>
    <div class="abs copyright">© copyright Copper Lantern Otter Works 2024</div>
  </footer>

</div>
</body>
</html>
```